Vantor - Adventurous, Fun, Exciting, Social Fitness Club needs a Webpage with attitude!

Vantor... we're a fun, social, outdoor fitness club that needs not just a homepage designed for our website, but in the process a "personality" for our unique, innovative and cheeky brand.
We pride ourselves on getting our members outdoors trying new, exciting physical activities in an effort to find joy in an active lifestyle, and sharing that experience with other like minded people. We offer:
- Personal Training (1-on-1 Fitness Training)
- Group Fitness Classes (Boxing, Pilates, etc)
- Boot Camps (Military Style - Sandbags, Ropes, Tyres, etc)
- Events (Fun Runs, Triathlons, Ocean Swims, Treks, etc)
- Adventures(Machu Picchu Trek, Rock Climbing, Kayaking, etc)
Our tag line is 'No Judgements. No Limits!' The homepage should be exciting, adventurous and innovative, illustrating the values of our brand: possibility, thirst for life, personal accomplishment & freedom. It should be fun, friendly & inviting.
A few of our key benefits to members are:
- No Boring Workouts
- No Joining Fees or Long Term Contracts
- Results Guaranteed
The links below should give you a rough idea of the sort of "feel" we're after (vibrant, active, adventurous ).
http://www.pupiljourneys.com.au/
http://www.layoutgoblin.com/website-templates/31924.html
http://www.layoutgoblin.com/website-templates/32751.html
http://www.pivel.com/
Target Market(s)
Real, Everyday People - Men & Women (30:70) aged mainly between 21-40, who want a more exciting and enjoyable fitness experience than your typical gym offers.
Industry/Entity Type
Fitness
Requirements
Must have
- Strong, uplifting and motivating images of people enjoying fitness/physical activities outdoors

```html
<!DOCTYPE html>
<html lang="en">
<head>
<meta charset="utf-8">
<title>Vantor – Fitness</title>
<link href="https://fonts.googleapis.com/css2?family=Yanone+Kaffeesatz:wght@300;400;600&family=Dancing+Script:wght@600&family=Nunito:ital,wght@0,400;1,400&display=swap" rel="stylesheet">
<style>
  :root{
    --sun:#fcc21b;
    --cream:#fffdd6;
    --orange:#e85e0c;
    --flame:#e8411c;
    --gold-link:#f2a21e;
    --leaf:#6f9e1c;
    --lime:#8cc63f;
    --ocean:#2c5fa8;
    --rose:#e0364f;
    --panel:#fde88c;
    --ink:#2a2a2a;
    --white:#ffffff;
  }
  *{box-sizing:border-box;margin:0;padding:0}
  html,body{width:960px;height:1200px;overflow:hidden}
  body{
    position:relative;
    background:linear-gradient(180deg,#fdd23a 0%,var(--sun) 40%,#fbb817 100%);
    font-family:"Nunito",sans-serif;color:var(--ink);
  }
  .abs{position:absolute}
  .page-shape{left:0;top:0}
  .brand{left:128px;top:72px;display:flex;align-items:center;gap:12px}
  .brand-dot{width:34px;height:34px;border-radius:50%;background:var(--orange)}
  .brand-name{font-family:"Yanone Kaffeesatz",sans-serif;font-weight:600;font-size:64px;color:var(--orange);line-height:1;letter-spacing:1px}
  .tagline{right:164px;top:70px;font-family:"Dancing Script",cursive;font-weight:600;font-size:21px;color:var(--flame);white-space:nowrap}
  .util-nav{top:106px;font-family:"Yanone Kaffeesatz",sans-serif;font-weight:300;font-size:19px;color:var(--gold-link)}
  .util-nav.login{text-decoration:underline}
  .caret{font-size:9px;vertical-align:middle;margin-left:3px}
  .main-nav .tab{
    position:absolute;top:194px;height:29px;
    background:linear-gradient(180deg,#fff176 0%,#fde03a 100%);
    border:1px solid #f5c400;border-bottom:none;
    font-family:"Yanone Kaffeesatz",sans-serif;font-weight:400;font-size:24px;font-variant:small-caps;
    color:var(--flame);text-align:center;line-height:29px;
    clip-path:polygon(0 0,92% 0,100% 30%,100% 100%,0 100%);
  }
  .main-nav .tab.active{color:var(--lime);background:linear-gradient(180deg,#f5fbb0 0%,#e3f27a 100%)}
  .amp{color:var(--sun)}
  .nav-rule{left:149px;top:223px;width:670px;height:2px;background:var(--orange)}
  .strip{background:var(--sun)}
  .hero{left:170px;top:253px;width:412px;height:260px;border:6px solid var(--leaf);
    background:linear-gradient(180deg,#1d56b8 0%,#3a86dd 55%,#7cb3ea 76%,#7aa83a 82%,#4f8a1f 100%)}
  .hero-title{left:16px;top:8px;font-family:"Yanone Kaffeesatz",sans-serif;font-weight:400;color:var(--white);font-size:24px;line-height:1.05}
  .hero-sub{font-size:19px}
  .hero-quote{left:12px;bottom:10px;font-family:"Yanone Kaffeesatz",sans-serif;color:var(--white);font-size:17px}
  .offer{left:590px;top:252px;width:204px;height:261px;background:var(--orange);color:var(--white);
    font-family:"Yanone Kaffeesatz",sans-serif}
  .offer h2{position:absolute;left:9px;top:8px;font-weight:400;font-size:22px;white-space:nowrap}
  .offer .valued{position:absolute;left:70px;top:34px;font-size:14px}
  .offer ul{position:absolute;left:10px;top:69px;list-style:none}
  .offer li{display:flex;align-items:center;gap:7px;font-size:15px;height:27px;white-space:nowrap}
  .field{position:absolute;left:24px;width:154px;height:17px;background:var(--white);border:1px solid #f0c9a8;
    font-family:"Nunito",sans-serif;font-size:10px;color:#aaa;padding-left:4px;line-height:15px}
  .join-btn{position:absolute;left:129px;top:230px;width:48px;height:17px;background:linear-gradient(#a8dc4a,#6aa51b);
    border:1px solid #cbe98a;font-size:14px;text-align:center;line-height:15px;color:var(--white)}
  .burst{position:absolute;left:135px;top:3px}
  .card{top:536px;height:262px;border:5px solid}
  .card .photo{position:absolute;inset:0}
  .card .label{position:absolute;left:12px;top:8px;font-family:"Yanone Kaffeesatz",sans-serif;color:var(--white);font-size:15px;line-height:1.2;white-space:nowrap}
  .badge{position:absolute;border-radius:50%;border:3px solid var(--white);color:var(--white);
    font-family:"Yanone Kaffeesatz",sans-serif;text-align:center;line-height:1;display:flex;flex-direction:column;
    justify-content:center;align-items:center;transform:rotate(-12deg);box-shadow:2px 3px 5px rgba(0,0,0,.35)}
  .more-btn{position:absolute;left:134px;top:34px;width:40px;height:14px;border:1px solid var(--white);
    background:#6f8fb8;color:var(--white);font-family:"Yanone Kaffeesatz",sans-serif;font-size:12px;text-align:center;line-height:12px}
  .info{left:164px;top:820px;width:638px;height:324px;background:var(--panel)}
  .copy{left:190px;width:290px}
  .copy h3{font-family:"Yanone Kaffeesatz",sans-serif;font-weight:400;font-size:17px;color:var(--ink);margin-bottom:4px}
  .copy p{font-size:9.6px;line-height:10.6px;margin-bottom:10px}
  .video{left:489px;top:832px;width:294px;height:201px;background:#fff8d8;border-radius:9px}
  .video .still{position:absolute;left:10px;top:10px;width:273px;height:180px;
    background:linear-gradient(180deg,#8fb1c7 0%,#9bb864 45%,#6d9a3c 100%)}
  .caption{left:500px;top:1047px;width:280px;font-style:italic;font-size:9.6px;line-height:10.6px}
  .footer{left:149px;top:1174px;width:671px;height:26px;background:var(--orange);
    display:flex;justify-content:center;gap:27px;align-items:center;
    font-family:"Yanone Kaffeesatz",sans-serif;font-size:12px;color:var(--white)}
</style>
</head>
<body>

<svg class="abs page-shape" width="960" height="1200" viewBox="0 0 960 1200" aria-hidden="true">
  <polygon points="146,66 822,6 822,1200 146,1200" fill="#f7941d"/>
  <polygon points="150,68 818,10 818,1200 150,1200" fill="var(--cream)"/>
</svg>

<header>
  <div class="abs brand"><span class="brand-dot"></span><span class="brand-name">Vantor</span></div>
  <p class="abs tagline">No Judgements. No Limits!</p>
  <a class="abs util-nav" style="left:568px">timetable</a>
  <a class="abs util-nav" style="left:644px">club locations<span class="caret">▼</span></a>
  <a class="abs util-nav login" style="left:750px">login</a>
  <nav class="main-nav">
    <a class="tab" style="left:178px;width:107px">Home</a>
    <a class="tab" style="left:293px;width:107px">About us</a>
    <a class="tab active" style="left:409px;width:107px">Fitness</a>
    <a class="tab" style="left:523px;width:141px">Events<span class="amp">&amp;</span>Adventures</a>
    <a class="tab" style="left:671px;width:107px">Contact us</a>
  </nav>
  <div class="abs nav-rule"></div>
</header>

<main>
  <div class="abs strip" style="left:164px;top:258px;width:638px;height:250px"></div>
  <div class="abs strip" style="left:180px;top:246px;width:608px;height:274px"></div>

  <section class="abs hero" role="img" aria-label="Photo of a woman leaping across a grassy field under a blue sky, trailing a long lime-green scarf">
    <h1 class="abs hero-title">Title<br><span class="hero-sub">subtitle</span></h1>
    <p class="abs hero-quote">Short testimonial/comment</p>
  </section>

  <aside class="abs offer">
    <h2>FREE Membership</h2>
    <span class="valued">(valued $65)</span>
    <svg class="burst" width="64" height="62" viewBox="0 0 70 66">
      <polygon fill="#e8202a" stroke="#fff" stroke-width="1.5" points="35,2 41,12 52,6 53,18 65,17 60,28 69,36 58,41 62,53 50,52 46,64 37,56 27,64 24,52 11,54 15,42 3,37 12,29 6,18 18,19 19,7 30,13"/>
      <text x="35" y="39" text-anchor="middle" transform="rotate(-18 35 35)" fill="#fff" font-family="Yanone Kaffeesatz, sans-serif" font-size="17">Join us!</text>
    </svg>
    <ul>
      <li><svg width="12" height="12" viewBox="0 0 24 24"><polygon fill="#fcc21b" points="12,1 15,9 23,9 17,14 19,23 12,18 5,23 7,14 1,9 9,9"/></svg>Monthly e-news hints, tips &amp; advice</li>
      <li><svg width="12" height="12" viewBox="0 0 24 24"><polygon fill="#fcc21b" points="12,1 15,9 23,9 17,14 19,23 12,18 5,23 7,14 1,9 9,9"/></svg>VIP invites events &amp; adventures</li>
      <li><svg width="12" height="12" viewBox="0 0 24 24"><polygon fill="#fcc21b" points="12,1 15,9 23,9 17,14 19,23 12,18 5,23 7,14 1,9 9,9"/></svg>Special member only offers</li>
      <li><svg width="12" height="12" viewBox="0 0 24 24"><polygon fill="#fcc21b" points="12,1 15,9 23,9 17,14 19,23 12,18 5,23 7,14 1,9 9,9"/></svg>Discounts card to 20+ providers</li>
    </ul>
    <div class="field" style="top:187px">Name</div>
    <div class="field" style="top:210px">E-mail</div>
    <div class="join-btn">Join us</div>
  </aside>

  <div class="abs strip" style="left:164px;top:542px;width:638px;height:250px"></div>
  <div class="abs strip" style="left:180px;top:530px;width:608px;height:274px"></div>

  <article class="abs card" style="left:170px;width:205px;border-color:var(--ocean)">
    <div class="photo" role="img" aria-label="Photo of two women stretching together on a park lawn at sunset" style="background:linear-gradient(180deg,#2f63b7 0%,#5d94d6 50%,#6a8d4a 78%,#3f6a22 100%)"></div>
    <p class="label">FREE Initial Consult<br>&amp; 1-on-1 Session</p>
    <div class="badge" style="left:134px;top:16px;width:52px;height:52px;background:#17b3a0;font-size:14px"><span>valued</span><span style="font-size:19px">$80</span></div>
  </article>

  <article class="abs card" style="left:381px;width:204px;border-color:var(--rose)">
    <div class="photo" role="img" aria-label="Photo of runners on a rocky trail with the sun low behind them" style="background:linear-gradient(180deg,#3d78c6 0%,#a9c7e4 45%,#f4f2e6 55%,#a8947a 75%,#6e5d49 100%)"></div>
    <p class="label" style="left:8px;font-size:14px">Intro Pass $25 7 Days Unlimited classes</p>
    <div class="more-btn">more</div>
  </article>

  <article class="abs card" style="left:591px;width:204px;border-color:var(--leaf)">
    <div class="photo" role="img" aria-label="Snapshots of a group of smiling women at an outdoor boot camp and a woman doing push-ups on grass" style="background:linear-gradient(180deg,#6a8f3b 0%,#a7c57a 40%,#d8c9b3 60%,#6d8a3e 100%)"></div>
    <p class="label">Boot Camp - starts soon</p>
    <div class="badge" style="left:134px;top:10px;width:50px;height:50px;background:var(--lime);font-size:15px"><span>#'s</span><span>limited</span></div>
  </article>

  <div class="abs strip" style="left:164px;top:828px;width:638px;height:308px"></div>
  <div class="abs strip" style="left:180px;top:814px;width:608px;height:338px"></div>
  <section class="abs info"></section>

  <div class="abs copy" style="top:834px">
    <h3>Personal Trainers in Brisbane</h3>
    <p>If you are exercising and have committed a good chunk of time into your fitness, you want to make sure you get the best returns possible. This is where a personal trainer can help. In personal training sessions you will be pushed to achieve your personal best, meaning that you get the best results, both physically and mentally, from your fitness training.</p>
    <p>For those that are new to exercising, it can be difficult to know where to begin. Having a personal trainer on board will give you the guidance and support that you need. Those that enlist the help of a personal trainer often find that they achieve much better results than those that go it alone, and often in a much shorter space of time.</p>
  </div>
  <div class="abs copy" style="top:1012px">
    <h3>Personal Training Locations Around Brisbane</h3>
    <p>If you are lucky enough to enjoy Brisbane's perfect climate then you shouldn't miss the chance to do some outdoor exercise. In the CBD you can enjoy a before work session at the Harlow Street Parkland or the Riverside City Botanic Gardens. About fifteen minutes out of town is the Mt Kellan Botanic Gardens which boast themed gardens and excellent tracks for walking and running. With plenty of beautiful parks around Brisbane's CBD, you don't need to worry about missing out on training just because of your long work hours.</p>
  </div>

  <figure class="abs video">
    <div class="still" role="img" aria-label="Video still of four women in bright tank tops flexing their arms in a park"></div>
    <svg class="abs" style="left:117px;top:77px" width="52" height="52" viewBox="0 0 52 52" aria-label="Play video">
      <circle cx="26" cy="26" r="25" fill="rgba(255,255,255,.45)"/>
      <polygon points="19,13 39,26 19,39" fill="#222" opacity=".8"/>
    </svg>
  </figure>
  <p class="abs caption">Just because you live in the suburbs, doesn't mean that you need to miss out on personal training either. Right around Brisbane and surrounds there are hundreds of personal trainers organizing classes in parks and in gyms and fitness studios.</p>
</main>

<footer class="abs footer">
  <a>About us</a><a>Club Locations</a><a>Terms and Conditions</a><a>Contact us</a>
</footer>

</body>
</html>
```